Design a Banner for my Adult Website (pleasure packs)

Hi there!

I am in need of 2 x simple banners for my adult website!
You can see the site here: www.velvetmoth.com.au

I have just invented a new category called "pleasure packs" ---> https://www.velvetmoth.com.au/pleasure-packs/

These items are just collections of existing products, put together for my customers to purchase with ease!

I am in need of a simple banner to go on the front page of my website (I've attached an existing banner here for your reference) + also a smaller graphic needed (also attached a sample)

The only requirement is that you use the words "Pleasure Packs" as the heading.. I'd like to also add "are here!" or "have arrived" or something like that on the banner.. but it's up to you - whatever looks good.

As for images & style, this is a competition so just looking to be inspired! Take a look at the other banners on my website for reference :-)

SIZES:
I hope I can create 2 x sizes for this banner:

SIZE 1: 1278 x 460 (example attached)
SIZE 2: 1138 x 123 (example attached)

Any questions please ask me!!

```html
<!DOCTYPE html>
<html lang="en">
<head>
<meta charset="utf-8">
<title>Pleasure Packs Are Here – Velvet Moth</title>
<link rel="stylesheet" href="https://fonts.googleapis.com/css2?family=Bebas+Neue&family=Great+Vibes&display=swap">
<style>
  :root {
    --bg: #000000;
    --gold-light: #fff2a0;
    --gold-mid: #f7c21a;
    --gold-deep: #c97a06;
    --heading-shadow: #1d2c5c;
    --script: #ffffff;
    --copy-light: #e9e7e2;
    --copy-dark: #9c9a94;
    --button-top: #5a5a5a;
    --button-bottom: #1c1c1c;
    --button-edge: #6e6e6e;
    --button-text: #e4e4e4;
    --skin-light: #c98a5c;
    --skin-mid: #8a5233;
    --skin-dark: #2a150b;
    --product-light: #e8d6c6;
    --product-dark: #1a1a1a;
  }
  * { margin: 0; padding: 0; box-sizing: border-box; }
  html, body { width: 1200px; height: 432px; overflow: hidden; background: var(--bg); }
  .banner {
    position: relative;
    width: 1200px;
    height: 432px;
    background: var(--bg);
    overflow: hidden;
    font-family: "Bebas Neue", "Arial Narrow", sans-serif;
  }
  .model-photo {
    position: absolute;
    left: 0; top: 0;
    width: 330px; height: 432px;
    background:
      radial-gradient(ellipse 55% 60% at 45% 45%, var(--skin-light) 0%, var(--skin-mid) 55%, transparent 85%),
      linear-gradient(90deg, var(--skin-dark) 0%, #3d2114 60%, var(--bg) 100%);
  }
  .heading {
    position: absolute;
    left: 350px; top: 12px;
    padding: 0 8px 6px 6px;
    font-size: 118px;
    font-weight: 400;
    line-height: 1;
    letter-spacing: 1px;
    white-space: nowrap;
    background: linear-gradient(180deg, var(--gold-light) 0%, var(--gold-mid) 45%, var(--gold-deep) 100%);
    -webkit-background-clip: text;
    background-clip: text;
    color: transparent;
    filter: drop-shadow(-4px 5px 0 var(--heading-shadow)) drop-shadow(0 0 2px rgba(0,0,0,0.8));
  }
  .heading-tag {
    position: absolute;
    left: 820px; top: 78px;
    font-family: "Great Vibes", cursive;
    font-size: 86px;
    line-height: 1;
    color: var(--script);
    white-space: nowrap;
  }
  .intro {
    position: absolute;
    left: 340px; top: 154px;
    width: 390px;
    text-align: center;
    font-size: 42px;
    line-height: 56px;
    letter-spacing: 0.5px;
    background: linear-gradient(180deg, var(--copy-light) 0%, var(--copy-dark) 100%);
    -webkit-background-clip: text;
    background-clip: text;
    color: transparent;
  }
  .cta {
    position: absolute;
    left: 355px; top: 345px;
    width: 387px; height: 80px;
    display: flex;
    align-items: center;
    justify-content: center;
    border-radius: 8px;
    border: 1px solid var(--button-edge);
    background: linear-gradient(180deg, var(--button-top) 0%, #333 50%, var(--button-bottom) 100%);
    color: var(--button-text);
    font-size: 44px;
    letter-spacing: 1px;
    text-decoration: none;
    padding-top: 4px;
  }
  .products-photo {
    position: absolute;
    left: 772px; top: 188px;
    width: 358px; height: 232px;
    border-radius: 4px;
    background:
      linear-gradient(90deg, var(--product-light) 0%, #c9b6a6 40%, #3a3a3a 48%, #d8d8d8 75%, var(--product-dark) 100%);
    opacity: 0.85;
  }
</style>
</head>
<body>
  <section class="banner">
    <div class="model-photo" role="img" aria-label="Photo of a shirtless man in open denim jeans against a dark wooden background"></div>
    <h1 class="heading">PLEASURE PACKS</h1>
    <p class="heading-tag">Are Here</p>
    <p class="intro">We've picked the very best<br>products to create these<br>easy to buy kits</p>
    <a class="cta" href="https://www.velvetmoth.com.au/pleasure-packs/">VIEW THE RANGE NOW!</a>
    <div class="products-photo" role="img" aria-label="Product lineup: a flesh-toned toy, lubricant and comfort spray bottles, a toy cleaner spray and a black douche bulb"></div>
  </section>
</body>
</html>
```